Marlowe Sail Works President Business Card Carbon fiber catamarans

Hi.. I need a new business card design.. I am the President of a high tech yacht builder. We build Carbon Fiber go fast catamarans... Maybe we use the file I am sharing to you as the back of the card.. We need to look cool and crisp ...

Target Market(s)

Affluent People who will purchase a cool yacht

Industry/Entity Type

Custom Yacht Builder

Contact Information for Business Card

Dean Pellington , President, 512.608.3419 USA

Font styles to use
Serif

Requirements
Must have
• the clean crisp cool feel
Nice to have
• clean and crisp
Should not have
• Bold ugly

```html
<!DOCTYPE html>
<html lang="en">
<head>
<meta charset="utf-8">
<title>Marlowe Sail Works – Business Card</title>
<link rel="stylesheet" href="https://fonts.googleapis.com/css2?family=Michroma&family=Source+Sans+3:wght@400&display=swap">
<style>
  :root {
    --backdrop: #2a2a2b;
    --card: #1f2022;
    --card-back-dark: #0b0b0c;
    --card-back-mid: #2b2b2d;
    --card-back-light: #6e6e70;
    --silver: #d9dadc;
    --silver-soft: #b9babd;
    --rule: #55575b;
    --icon-tile: #c9cacc;
    --icon-ink: #2a2b2d;
  }
  * { margin: 0; padding: 0; box-sizing: border-box; }
  html, body {
    width: 1200px; height: 1108px; overflow: hidden;
    background: var(--backdrop);
  }
  .canvas {
    position: relative; width: 1200px; height: 1108px;
    display: flex; justify-content: center; align-items: center; gap: 60px;
  }
  .card {
    width: 440px; height: 680px; border-radius: 22px;
    box-shadow: 0 18px 40px rgba(0,0,0,.45);
    position: relative; overflow: hidden;
  }
  .card-front {
    background: var(--card);
    display: flex; flex-direction: column; align-items: center;
    font-family: "Source Sans 3", sans-serif; color: var(--silver-soft);
  }
  .brand {
    margin-top: 96px;
    display: flex; align-items: center; gap: 16px;
  }
  .brand-mark { width: 18px; height: 18px; background: var(--silver); }
  .brand-name {
    font-family: "Michroma", sans-serif; color: var(--silver);
    font-size: 21px; letter-spacing: 2px; text-transform: uppercase; line-height: 1.3;
  }
  .person { margin-top: 150px; text-align: center; }
  .person-name {
    font-family: "Michroma", sans-serif; color: var(--silver);
    font-size: 19px; letter-spacing: 3px; text-transform: uppercase;
  }
  .person-title { font-size: 20px; margin-top: 2px; }
  .icon-row {
    margin-top: 16px; width: 300px;
    display: flex; align-items: center; gap: 8px;
  }
  .icon-row .rule { flex: 1; height: 1px; background: var(--rule); }
  .icon-tile {
    width: 28px; height: 28px; border-radius: 4px; background: var(--icon-tile);
    display: flex; align-items: center; justify-content: center;
  }
  .contact { margin-top: 10px; text-align: center; font-size: 21px; line-height: 1.35; }
  .contact .phone { color: var(--silver); }
  .divider { width: 300px; height: 1px; background: var(--rule); margin: 14px 0; }
  .address { font-size: 21px; }
  .card-back {
    background:
      radial-gradient(ellipse at 90% 5%, var(--card-back-light) 0%, var(--card-back-mid) 40%, var(--card-back-dark) 80%);
  }
</style>
</head>
<body>
<main class="canvas">
  <section class="card card-front">
    <div class="brand">
      <span class="brand-mark"></span>
      <span class="brand-name">Marlowe<br>Sail Works</span>
    </div>
    <div class="person">
      <p class="person-name">Dean Pellington</p>
      <p class="person-title">President</p>
    </div>
    <div class="icon-row">
      <span class="rule"></span>
      <span class="icon-tile">
        <svg width="18" height="18" viewBox="0 0 24 24"><path fill="var(--icon-ink)" d="M6.6 10.8a15 15 0 0 0 6.6 6.6l2.2-2.2c.3-.3.7-.4 1-.2 1.1.4 2.3.6 3.6.6.6 0 1 .4 1 1V20c0 .6-.4 1-1 1A17 17 0 0 1 3 4c0-.6.4-1 1-1h3.5c.6 0 1 .4 1 1 0 1.3.2 2.5.6 3.6.1.3 0 .7-.2 1z"/></svg>
      </span>
      <span class="icon-tile">
        <svg width="18" height="18" viewBox="0 0 24 24"><rect x="3" y="6" width="18" height="12" fill="none" stroke="var(--icon-ink)" stroke-width="2"/><path d="M3 6l9 7 9-7" fill="none" stroke="var(--icon-ink)" stroke-width="2"/></svg>
      </span>
      <span class="icon-tile">
        <svg width="18" height="18" viewBox="0 0 24 24"><circle cx="12" cy="12" r="9" fill="none" stroke="var(--icon-ink)" stroke-width="2"/><path d="M3 12h18M12 3c3 3 3 15 0 18M12 3c-3 3-3 15 0 18" fill="none" stroke="var(--icon-ink)" stroke-width="1.5"/></svg>
      </span>
      <span class="rule"></span>
    </div>
    <div class="contact">
      <p class="phone">512.608.3419</p>
      <p>info@marlowesail.com</p>
      <p>www.marlowesailworks.com</p>
    </div>
    <div class="divider"></div>
    <p class="address">Texas 78701, USA</p>
  </section>
  <section class="card card-back" role="img" aria-label="Repeating pattern of glossy shield emblems fading from silver to black"></section>
</main>
</body>
</html>
```